Starting meadery needs logo and label design

We are starting to show our hand crafted meads to potential investors and need a professional logo and label to properly show how serious this proj...

Target Market(s)

Craft beer drinker searching for a new experience. People who are beer drinkers aspiring to be wine drinker.

Industry/Entity Type

It Professional

Requirements
Must have
• Professional design. Not overly ornate. Simple use of colors for low cost startup printing.

```html
<!DOCTYPE html>
<html lang="en">
<head>
<meta charset="UTF-8">
<title>Larkhollow Meadery – Orange Blossom Mead Label</title>
<link rel="stylesheet" href="https://fonts.googleapis.com/css2?family=Josefin+Sans:wght@700&family=Poppins:wght@500&family=Satisfy&display=swap">
<style>
  :root {
    --sky: #dfecf6;
    --ink: #141414;
    --honey-brown: #8a5419;
    --gold: #c9ab45;
    --paper: #ffffff;
  }
  html, body {
    margin: 0;
    padding: 0;
    overflow: hidden;
  }
  .label {
    position: relative;
    width: 901px;
    height: 1200px;
    background: var(--sky);
    overflow: hidden;
  }
  .brand {
    position: absolute;
    left: 0;
    top: 40px;
    width: 901px;
    height: 640px;
    display: flex;
    flex-direction: column;
    align-items: center;
    justify-content: center;
    gap: 34px;
  }
  .brand-dot {
    width: 110px;
    height: 110px;
    border-radius: 50%;
    background: var(--gold);
  }
  .brand-name {
    font-family: "Josefin Sans", sans-serif;
    font-weight: 700;
    font-size: 118px;
    letter-spacing: 3px;
    color: var(--honey-brown);
    margin: 0;
    line-height: 1.05;
    text-align: center;
    text-transform: uppercase;
  }
  .variety {
    position: absolute;
    left: 0;
    top: 722px;
    width: 901px;
    margin: 0;
    text-align: center;
    font-family: "Poppins", sans-serif;
    font-weight: 500;
    font-size: 56px;
    line-height: 1;
    color: var(--ink);
  }
  .product {
    position: absolute;
    left: 0;
    top: 796px;
    width: 901px;
    margin: 0;
    text-align: center;
    font-family: "Josefin Sans", sans-serif;
    font-weight: 700;
    font-size: 150px;
    line-height: 1;
    letter-spacing: 22px;
    padding-left: 22px;
    box-sizing: border-box;
    color: var(--ink);
    text-shadow: 4px 4px 0 var(--paper), 8px 8px 0 var(--ink);
  }
  .description {
    position: absolute;
    left: 20px;
    top: 978px;
    width: 861px;
    margin: 0;
    text-align: center;
    font-family: "Satisfy", "Dancing Script", "Brush Script MT", cursive;
    font-size: 29px;
    line-height: 52px;
    color: var(--ink);
    white-space: nowrap;
  }
</style>
</head>
<body>
  <main class="label">
    <header class="brand">
      <span class="brand-dot"></span>
      <p class="brand-name">Larkhollow<br>Meadery</p>
    </header>
    <h2 class="variety">Orange blossom</h2>
    <h1 class="product">MEAD</h1>
    <p class="description">Lorem ipsum dolor sit amet, Lorem ipsum dolor sit amet,<br>consectetuer adipiscing elit, sed diam nonummy nibh<br>euismod tincidunt ut laoreet dolore magna aliquam erat<br>volutpat. Ut wisi enim ad minim veniam, quis nostrud</p>
  </main>
</body>
</html>
```